Webdesign für Wandertouren
Hi Wenke, thank you very much for the wonderful and successful collaboration. I was very pleased that you contributed your ideas so well. I'm really happy with your design and I'm looking forward to the reactions of my guests. I wish you many great clients and a lot of success in the future. Best regards Rieke
Zielgruppe
Liebe Designende, wunderbar, dass Du hier gelandet bist.
Ich biete als International Mountain Leader
Wandertouren, Trekkingreisen und Naturerlebnisse - regional und international an. Die Touren werden (noch alle) von mir persönlich durchgeführt.
Hier der Einstiegstext für die Startseite.
Atemberaubende Landschaften mit majestätischen Bergen, wunderschönen Hochebenen und beeindruckenden Wasserfällen verzaubern Deine Seele.
Wandertouren, Trekkingreisen und Naturerlebnisse führen Dich in fantastische Paradieswelten. Hier erlebst Du eindrucksvolle Glücksgefühle. Gerührt von der Schönheit und der Einzigartigkeit der wundervollen Natur kannst Du Dich tief entspannen und die Gegenwart genießen.
On Top gibt es dazu urige Berghütten und inspirierende Begegnungen, die Deine Bergabenteuer zu wundervollen Erlebnissen für Dich machen.
Und hast Du schon Lust bekommen mitzukommen?
Zielgruppe: Frauen und Männer zwischen 38 - 65 Jahren
Aufgabenstellung
*Ich liebe den Hintergrund mit altem Holz, dazu schicke ich Bilder mit. Mehr kann ich dann noch im Verlauf des Projektes schicken, da ich nur 10 Bilder auf einmal hochladen kann.
*Ich schicke Bilder aus einem Smoothie Rezept Buch, JPG 5465 das finde ich witzig um die Seite aufzulockern, vielleicht gibt es ja Ideen dazu wie es umgesetzt werden kann. - Dementsprechend möchte ich diese Elemente auch in dem Flyerprojekt im Anschluß umgesetzt haben.
Kräftige Farben sind gewünscht. Pink ist eh in meinem Logo. Gerne auch ein helles Lindgrün.

```html
<!DOCTYPE html>
<html lang="de">
<head>
<meta charset="utf-8">
<title>Menü – Wandertouren</title>
<link rel="stylesheet" href="https://fonts.googleapis.com/css2?family=Raleway:wght@500;600&display=swap">
<style>
  :root {
    --pink: #ec1c69;
    --white: #ffffff;
  }
  html, body {
    margin: 0;
    padding: 0;
    overflow: hidden;
  }
  .menu-screen {
    position: relative;
    width: 1200px;
    height: 675px;
    background: var(--pink);
    overflow: hidden;
    font-family: "Raleway", sans-serif;
  }
  .close-button {
    position: absolute;
    left: 1025px;
    top: 35px;
    width: 50px;
    height: 50px;
  }
  .main-nav {
    position: absolute;
    left: 369px;
    top: 126px;
    margin: 0;
    padding: 0;
    list-style: none;
  }
  .main-nav li {
    height: 71px;
    line-height: 36px;
  }
  .main-nav a {
    color: var(--white);
    text-decoration: none;
    font-weight: 600;
    font-size: 22px;
    letter-spacing: 0.24em;
    text-transform: uppercase;
    white-space: nowrap;
  }
</style>
</head>
<body>
  <div class="menu-screen">
    <svg class="close-button" viewBox="0 0 50 50" aria-label="Menü schließen">
      <circle cx="25" cy="25" r="25" fill="var(--white)"/>
      <path d="M17 17 L33 33 M33 17 L17 33" stroke="var(--pink)" stroke-width="4.5" stroke-linecap="round"/>
    </svg>
    <ul class="main-nav">
      <li><a href="#">Bergabenteuer erleben</a></li>
      <li><a href="#">Gipfelglück genießen</a></li>
      <li><a href="#">Verzaubern lassen</a></li>
      <li><a href="#">Gemeinsam unterwegs sein</a></li>
      <li><a href="#">Dein Guide Rieke</a></li>
    </ul>
  </div>
</body>
</html>
```